Redesign Opal's RV Park & Lodge Website, Leeds, North Dakota

I need a totally re-designed website for my RV Park / Lodge. I want to not only provide information on my RV Park / Lodge, I want to provide my customers with information on the town and area attractions. I want to provide rate information. Ideally, I would like to have a button/page for each section: Welcome & Information, Area Attractions, Welcome to Leeds, Rates, Who's Opal?!, FAQ's and Where are we?. I don't know if this would be more expensive the more pages you have? If more pages is too expensive, then we can combine info on less pages. I want my logo included on the web page. I want Mockup Forge to take down my old website and use the same address to put up my newly designed website.

Target Market(s)

Full time RVers, People who camp, hunt fish, People who recreate on Devils Lake, People who are looking for meeting/conference space, people who are looking for party venue

Industry/Entity Type

Accommodation

Number of Pages Required

3 page

Requirements
Must have
• I want a cozy, welcoming type web site. No super dark colors. Bright and cheerful.
• Must be simple and organized.
• NOTE: I have a file of pictures of the interior of Opal's Lodge that must be included in website. Please request this file if you will be designing my project as the files are too large to upload through Mockup Forge.
Nice to have
• If you cannot open any of the files listed, please notify me.
Should not have
• No stark or super-formal designs.

```html
<!DOCTYPE html>
<html lang="en">
<head>
<meta charset="utf-8">
<title>Opal's RV Park &amp; Lodge</title>
<link rel="stylesheet" href="https://fonts.googleapis.com/css2?family=Lato:wght@400;700;900&display=swap">
<style>
:root{
  --red:#b5162b;
  --red-dark:#9c1124;
  --peach:#f2a27b;
  --ink:#1d1d1d;
  --text:#555;
  --muted:#888;
  --line:#d9d9d9;
  --footer:#1b1b1b;
  --white:#fff;
}
*{box-sizing:border-box;margin:0;padding:0}
html,body{width:1200px;height:4045px;overflow:hidden}
body{font-family:'Lato',sans-serif;color:var(--text);background:var(--white);position:relative}

/* header */
.topline{position:absolute;top:0;left:0;width:1200px;height:5px;background:var(--red)}
.contact-bar{position:absolute;top:14px;right:100px;font-size:14px;color:#444;display:flex;gap:28px;align-items:center}
.contact-bar span{display:flex;align-items:center;gap:7px}
.nav{position:absolute;top:56px;left:310px;right:97px;display:flex;justify-content:space-between;font-size:14px;color:#333;align-items:center;white-space:nowrap}
.nav a{color:inherit;text-decoration:none}
.nav a.active{color:var(--red)}
.brand{position:absolute;left:72px;top:6px;width:196px;height:196px;border-radius:50%;background:var(--white);z-index:5;display:flex;align-items:center;justify-content:center;text-align:center;box-shadow:0 2px 6px rgba(0,0,0,.12)}
.brand-name{font-weight:700;font-size:21px;line-height:1.25;color:var(--ink);padding-top:30px}

/* hero */
.hero{position:absolute;top:95px;left:0;width:1200px;height:560px;overflow:hidden}
.hero-photo{position:absolute;inset:0;background:linear-gradient(180deg,#7e97ad 0%,#a9b7c0 35%,#8c3a3a 55%,#6c7a4a 75%,#4f5e33 100%)}
.hero-shade{position:absolute;inset:0;background:rgba(20,20,30,.35)}
.hero h1{position:absolute;top:140px;width:100%;text-align:center;color:var(--white);font-weight:900;font-size:64px;letter-spacing:1px}
.hero p{position:absolute;top:230px;width:100%;text-align:center;color:var(--white);font-size:24px;font-weight:700}
.btn-ghost{position:absolute;border:2px solid var(--white);color:var(--white);border-radius:30px;font-size:15px;font-weight:700;letter-spacing:.5px;display:flex;align-items:center;justify-content:center}
.hero .btn-ghost{top:285px;left:510px;width:180px;height:50px}
.dots{position:absolute;top:440px;left:568px;display:flex;gap:6px}
.dots i{width:14px;height:14px;border-radius:50%;border:2px solid var(--white)}
.dots i:first-child{background:var(--white)}
.hero-wave{position:absolute;top:470px;left:0;width:1200px;height:190px;z-index:2}

/* welcome */
.welcome h2{position:absolute;top:725px;width:1200px;text-align:center;font-size:35px;font-weight:900;color:var(--ink);line-height:1.35}
.welcome p{position:absolute;top:838px;left:175px;width:850px;text-align:center;font-size:15px;line-height:1.8;color:var(--muted)}
.rule{position:absolute;top:950px;left:97px;width:1006px;height:1px;background:var(--line)}

/* meeting */
.meeting h2{position:absolute;top:1024px;left:97px;font-size:35px;font-weight:900;color:var(--ink)}
.meeting p{position:absolute;left:97px;width:530px;font-size:15px;line-height:1.85;color:var(--muted)}
.btn-outline{position:absolute;border:2px solid var(--red);color:var(--red);border-radius:30px;font-size:13px;font-weight:900;display:flex;align-items:center;justify-content:center;letter-spacing:.5px}
.meeting-photo{position:absolute;top:1018px;left:674px;width:428px;height:362px;background:linear-gradient(160deg,#7a1d25 0%,#a24a4c 40%,#d9d5dc 70%,#5a6a8a 100%);border:4px solid #eee}

/* lodge */
.lodge{position:absolute;top:1464px;left:0;width:1200px;height:500px}
.lodge-photo{position:absolute;left:0;top:0;width:600px;height:500px;background:linear-gradient(120deg,#7b4b3b 0%,#c7a88a 35%,#efe6d6 60%,#4e3b30 100%)}
.lodge-panel{position:absolute;left:600px;top:0;width:600px;height:500px;background:var(--red)}
.lodge-panel h2{position:absolute;top:50px;left:46px;font-size:32px;font-weight:900;color:var(--white)}
.lodge-panel p{position:absolute;top:110px;left:46px;width:500px;font-size:15px;line-height:1.75;color:var(--white)}
.ticks{position:absolute;top:178px;left:46px;list-style:none;color:var(--white);font-size:15px}
.ticks li{display:flex;align-items:center;gap:10px;height:29px}
.lodge-panel .btn-ghost{top:400px;left:46px;width:136px;height:46px;font-size:13px;font-weight:900}

/* rv park */
.rv h2{position:absolute;top:2035px;width:1200px;text-align:center;font-size:35px;font-weight:900;color:var(--ink)}
.rv p{position:absolute;top:2100px;left:300px;width:600px;text-align:center;font-size:15px;line-height:1.8;color:var(--muted)}
.features{position:absolute;top:2200px;left:97px;width:1006px;display:flex;justify-content:space-between}
.feature{width:196px;text-align:center}
.feature-ring{width:164px;height:164px;border-radius:50%;border:3px solid var(--red);margin:0 auto;display:flex;align-items:center;justify-content:center}
.feature-core{width:140px;height:140px;border-radius:50%;background:var(--white);box-shadow:0 0 0 2px #f1d4d8 inset;display:flex;align-items:center;justify-content:center}
.feature h3{margin-top:22px;font-size:19px;font-weight:400;color:var(--ink);line-height:1.35;white-space:nowrap}

/* tents */
.tents{position:absolute;top:2503px;left:0;width:1200px;height:172px;background:var(--peach);text-align:center;color:var(--white)}
.tents h2{margin-top:40px;font-size:35px;font-weight:900}
.tents p{margin-top:10px;font-size:22px;font-weight:700}

/* reviews */
.reviews{position:absolute;top:2675px;left:0;width:1200px;height:345px;overflow:hidden}
.reviews-photo{position:absolute;inset:0;background:linear-gradient(100deg,#2e3a3a 0%,#5f6c66 40%,#b08c62 75%,#7a5b3b 100%)}
.reviews-shade{position:absolute;inset:0;background:rgba(0,0,0,.3)}
.reviews h2{position:absolute;top:65px;width:100%;text-align:center;color:var(--white);font-size:35px;font-weight:900;line-height:1.3}
.reviews p{position:absolute;top:180px;width:100%;text-align:center;color:var(--white);font-size:24px;font-weight:700}
.reviews .btn-ghost{top:232px;left:522px;width:156px;height:48px;font-size:16px;gap:8px}

/* rates */
.rates h2{position:absolute;top:3090px;width:1200px;text-align:center;font-size:35px;font-weight:900;color:var(--ink)}
.rate-card{position:absolute;top:3166px;width:316px;height:345px;border:1px solid #bbb;padding:30px 26px}
.rate-card h3{font-size:20px;font-weight:900;color:var(--ink);margin-bottom:30px}
.rate-card p{font-size:14px;line-height:1.85;color:var(--text);margin-bottom:24px}
.rate-card.featured{background:var(--red);border-color:var(--red)}
.rate-card.featured h3,.rate-card.featured p{color:var(--white)}

/* footer */
.footer-wave{position:absolute;top:3620px;left:0;width:1200px;height:100px}
.footer{position:absolute;top:3700px;left:0;width:1200px;height:345px;background:var(--footer);color:var(--white)}
.footer-brand{position:absolute;top:40px;left:97px;width:180px;font-size:24px;font-weight:700;line-height:1.3;text-align:center}
.footer h4{position:absolute;top:48px;font-size:17px;font-weight:900;letter-spacing:.5px}
.links{position:absolute;top:88px;left:350px;list-style:none;font-size:13px;line-height:1.85}
.newsletter p{position:absolute;top:88px;left:555px;width:250px;font-size:13px;line-height:1.7}
.email-box{position:absolute;top:140px;left:555px;width:255px;height:34px;background:var(--white);color:#777;font-size:12px;padding:10px}
.subscribe{position:absolute;top:188px;left:555px;width:108px;height:34px;border-radius:20px;background:var(--red);font-size:12px;font-weight:700;display:flex;align-items:center;justify-content:center}
.contact-list{position:absolute;top:94px;left:896px;list-style:none;font-size:13px}
.contact-list li{display:flex;gap:16px;margin-bottom:22px;line-height:1.6}
.footer-rule{position:absolute;top:278px;left:97px;width:1006px;height:1px;background:#3a3a3a}
.copyright{position:absolute;top:305px;left:97px;font-size:13px}
.socials{position:absolute;top:296px;left:958px;display:flex;gap:10px}
.socials i{width:30px;height:30px;border-radius:50%;border:1px solid #aaa}
</style>
</head>
<body>

<header>
  <div class="topline"></div>
  <div class="contact-bar">
    <span><svg width="14" height="14" viewBox="0 0 24 24"><path fill="#b5162b" d="M6.6 10.8a15 15 0 006.6 6.6l2.2-2.2a1 1 0 011-.25 11 11 0 003.5.56 1 1 0 011 1V20a1 1 0 01-1 1A17 17 0 013 4a1 1 0 011-1h3.5a1 1 0 011 1 11 11 0 00.56 3.5 1 1 0 01-.25 1z"/></svg>701-555-0142 | 701-555-0187</span>
    <span><svg width="16" height="12" viewBox="0 0 16 12"><rect width="16" height="12" rx="1" fill="#b5162b"/><path d="M1 1l7 5 7-5" stroke="#fff" fill="none"/></svg>stay@opalsrvpark.example</span>
  </div>
  <div class="brand"><div class="brand-name">Opal's RV Park<br>&amp; Lodge<br>Leeds ND</div></div>
  <nav class="nav">
    <a class="active">Home</a><a>Welcome &amp; Information</a><a>Area Attractions</a><a>Welcome to Leeds</a><a>Rates</a><a>Who's Opal?!</a><a>FAQ's</a><a>Where are we</a>
    <svg width="15" height="15" viewBox="0 0 16 16"><circle cx="6.5" cy="6.5" r="5" stroke="#333" stroke-width="2" fill="none"/><path d="M10 10l5 5" stroke="#333" stroke-width="2"/></svg>
  </nav>
</header>

<section class="hero">
  <div class="hero-photo" role="img" aria-label="Red lodge building with covered porch under a wide prairie sky"></div>
  <div class="hero-shade"></div>
  <h1>OPAL RV PARK &amp; LOGDE</h1>
  <p>Heart of some of the greatest hunting and fishing in the world</p>
  <div class="btn-ghost">GET MORE INFO</div>
  <div class="dots"><i></i><i></i><i></i><i></i></div>
</section>
<svg class="hero-wave" viewBox="0 0 1200 190" preserveAspectRatio="none">
  <path d="M0 105 Q560 230 1200 15 L1200 190 L0 190Z" fill="#f2a27b"/>
  <path d="M0 125 Q560 245 1200 35 L1200 190 L0 190Z" fill="#fff"/>
</svg>

<section class="welcome">
  <h2>WELCOME TO OPAL'S RV PARK &amp; LODGE<br>AND LEEDS, NORTH DAKOTA</h2>
  <p>Leeds is in the heart of some of the greatest hunting and fishing in the world. Opal's RV Park is located right on Highway 2 midway between Devils Lake and Rugby North Dakota. We are smack dab in the middle of it all!</p>
  <div class="rule"></div>
</section>

<section class="meeting">
  <h2>MEETING / CONFERENCE SPACE</h2>
  <p style="top:1090px">Are you looking for a venue for your next meeting, training event, guys/girls weekend, quilt retreat, holiday gathering, family reunion, birthday, wedding party or get-together? We've got you covered! Opal's Lodge seats about 65 people comfortably.</p>
  <p style="top:1228px">Many of our customers have commented that Opal's was the perfect place for their event because it was so inviting....and just like home!</p>
  <div class="btn-outline" style="top:1317px;left:97px;width:136px;height:48px">READ MORE</div>
  <div class="meeting-photo" role="img" aria-label="Lodge meeting room set with tables, tablecloths and folding chairs"></div>
</section>

<section class="lodge">
  <div class="lodge-photo" role="img" aria-label="Cozy lodge living room with sofa, lamp and warm walls"></div>
  <div class="lodge-panel">
    <h2>OPAL'S LODGE</h2>
    <p>Are you looking for a cozy, but spacious home away from home? Well, you have found it! Opal's Lodge is 2200 square feet of living space.</p>
    <ul class="ticks">
      <li><svg width="15" height="15" viewBox="0 0 16 16"><circle cx="8" cy="8" r="8" fill="#fff"/><path d="M4.5 8.2l2.4 2.4 4.6-4.8" stroke="#b5162b" stroke-width="2" fill="none"/></svg>Groups - hunting, fishing, working, playing</li>
      <li><svg width="15" height="15" viewBox="0 0 16 16"><circle cx="8" cy="8" r="8" fill="#fff"/><path d="M4.5 8.2l2.4 2.4 4.6-4.8" stroke="#b5162b" stroke-width="2" fill="none"/></svg>2200 square feet</li>
      <li><svg width="15" height="15" viewBox="0 0 16 16"><circle cx="8" cy="8" r="8" fill="#fff"/><path d="M4.5 8.2l2.4 2.4 4.6-4.8" stroke="#b5162b" stroke-width="2" fill="none"/></svg>Full kitchen</li>
      <li><svg width="15" height="15" viewBox="0 0 16 16"><circle cx="8" cy="8" r="8" fill="#fff"/><path d="M4.5 8.2l2.4 2.4 4.6-4.8" stroke="#b5162b" stroke-width="2" fill="none"/></svg>Free WiFi</li>
      <li><svg width="15" height="15" viewBox="0 0 16 16"><circle cx="8" cy="8" r="8" fill="#fff"/><path d="M4.5 8.2l2.4 2.4 4.6-4.8" stroke="#b5162b" stroke-width="2" fill="none"/></svg>Satellite TV</li>
      <li><svg width="15" height="15" viewBox="0 0 16 16"><circle cx="8" cy="8" r="8" fill="#fff"/><path d="M4.5 8.2l2.4 2.4 4.6-4.8" stroke="#b5162b" stroke-width="2" fill="none"/></svg>2 restrooms, one is handicap accessible</li>
      <li><svg width="15" height="15" viewBox="0 0 16 16"><circle cx="8" cy="8" r="8" fill="#fff"/><path d="M4.5 8.2l2.4 2.4 4.6-4.8" stroke="#b5162b" stroke-width="2" fill="none"/></svg>A great room with ample seating for large groups</li>
    </ul>
    <div class="btn-ghost">READ MORE</div>
  </div>
</section>

<section class="rv">
  <h2>OPAL'S RV PARK</h2>
  <p>Opal's RV Park sits right next to Highway 2 on the north side. We have 14 full service spaces – sewer, water and electric (20, 30, 50 amp).</p>
  <div class="features">
    <div class="feature"><div class="feature-ring"><div class="feature-core">
      <svg width="56" height="56" viewBox="0 0 56 56"><circle cx="22" cy="30" r="12" fill="none" stroke="#b5162b" stroke-width="7" stroke-dasharray="5 3.4"/><circle cx="22" cy="30" r="8" fill="#b5162b"/><circle cx="22" cy="30" r="3.5" fill="#fff"/><circle cx="41" cy="15" r="7" fill="none" stroke="#b5162b" stroke-width="5" stroke-dasharray="3.5 2"/><circle cx="41" cy="15" r="2.5" fill="#b5162b"/></svg>
    </div></div><h3>14 Full<br>Service Spaces</h3></div>
    <div class="feature"><div class="feature-ring"><div class="feature-core">
      <svg width="44" height="56" viewBox="0 0 44 56"><path d="M26 2L6 32h14l-4 22 22-32H24z" fill="#b5162b"/></svg>
    </div></div><h3>Electric,<br>Water, Sewer</h3></div>
    <div class="feature"><div class="feature-ring"><div class="feature-core">
      <svg width="46" height="56" viewBox="0 0 46 56"><path d="M23 2L3 9v18c0 13 9 22 20 27 11-5 20-14 20-27V9z" fill="#b5162b"/><path d="M23 8v40c8-4 14-11 14-21V13z" fill="#fff"/></svg>
    </div></div><h3>Safe &amp;<br>convenient location</h3></div>
    <div class="feature"><div class="feature-ring"><div class="feature-core">
      <svg width="56" height="56" viewBox="0 0 56 56"><circle cx="28" cy="28" r="24" fill="#b5162b"/><circle cx="28" cy="28" r="18" fill="#fff"/><path d="M28 15v14h10" stroke="#b5162b" stroke-width="4" fill="none"/></svg>
    </div></div><h3>24 hour indoor<br>restroom with shower</h3></div>
    <div class="feature"><div class="feature-ring"><div class="feature-core">
      <svg width="56" height="56" viewBox="0 0 56 56"><circle cx="28" cy="28" r="25" fill="#b5162b"/><path d="M16 29l8 8 16-17" stroke="#fff" stroke-width="5" fill="none"/></svg>
    </div></div><h3>Gas station/<br>convenience</h3></div>
  </div>
</section>

<section class="tents">
  <h2>TENTS</h2>
  <p>Primitive &amp; tent sites are also available</p>
</section>

<section class="reviews">
  <div class="reviews-photo" role="img" aria-label="Angler casting a fishing rod at sunset"></div>
  <div class="reviews-shade"></div>
  <h2>WHAT OUR CUSTOMERS ARE SAYING ABOUT<br>OPAL'S RV PARK &amp; LODGE</h2>
  <p>Check out our Campfire Page</p>
  <div class="btn-ghost"><svg width="16" height="16"><rect width="16" height="16" rx="2" fill="#fff"/></svg>CAMPFIRE</div>
</section>

<section class="rates">
  <h2>RATES</h2>
  <div class="rate-card" style="left:97px">
    <h3>Opal's Lodge Pricing</h3>
    <p>$200 for 24 hours.<br>The first 6 adults are included in the $200 per night rent.</p>
    <p>Each adult exceeding the initial 6, must pay $25 per night. Kids under age 16 stay free.</p>
  </div>
  <div class="rate-card featured" style="left:442px">
    <h3>Opal's RV Park Pricing</h3>
    <p>RV Sites: $24/Night $125/Week $375/month This price is for 4 adults. Any adults exceeding the initial 4, must pay $5 extra per night. Kids under 16 stay free.</p>
    <p>Tent Sites: $12/Night<br>This price is for 4 adults. Any adults exceeding the initial 4, must pay $3 extra per night. Kids under 16 stay free.</p>
  </div>
  <div class="rate-card" style="left:787px">
    <h3>Showers</h3>
    <p>Showers are $5 per person for unregistered customers.</p>
    <p>There is no charge for anyone that uses the shower that is staying at Opal's RV Park &amp; Lodge.</p>
  </div>
</section>

<svg class="footer-wave" viewBox="0 0 1200 100" preserveAspectRatio="none">
  <path d="M0 100 Q600 -40 1200 100Z" fill="#f2a27b"/>
  <path d="M0 100 Q600 -15 1200 100Z" fill="#1b1b1b"/>
</svg>
<footer class="footer">
  <div class="footer-brand">Opal's RV Park<br>&amp; Lodge<br>Leeds ND</div>
  <h4 style="left:350px">QUICK LINKS</h4>
  <ul class="links"><li>Help</li><li>FAQ</li><li>Support</li><li>Sitemap</li><li>Terms Of Use</li><li>Privacy Statement</li></ul>
  <div class="newsletter">
    <h4 style="left:555px">NEWSLETTER SUBSCRIPTION</h4>
    <p>Register your Email Address to get information about us</p>
    <div class="email-box">Email Address</div>
    <div class="subscribe">SUBSCRIBE</div>
  </div>
  <h4 style="left:896px">CONTACT US</h4>
  <ul class="contact-list">
    <li><svg width="12" height="16" viewBox="0 0 12 16"><path d="M6 0a6 6 0 00-6 6c0 4.5 6 10 6 10s6-5.5 6-10a6 6 0 00-6-6z" fill="#fff"/><circle cx="6" cy="6" r="2.2" fill="#1b1b1b"/></svg>120 Prairie Rd Leeds ND 58300</li>
    <li><svg width="12" height="16" viewBox="0 0 24 24"><path fill="#fff" d="M6.6 10.8a15 15 0 006.6 6.6l2.2-2.2a1 1 0 011-.25 11 11 0 003.5.56 1 1 0 011 1V20a1 1 0 01-1 1A17 17 0 013 4a1 1 0 011-1h3.5a1 1 0 011 1 11 11 0 00.56 3.5 1 1 0 01-.25 1z"/></svg><span>701-555-0142<br>701-555-0187</span></li>
    <li><svg width="14" height="12" viewBox="0 0 16 12"><rect width="16" height="12" rx="1" fill="#fff"/><path d="M1 1l7 5 7-5" stroke="#1b1b1b" fill="none"/></svg>stay@opalsrvpark.example</li>
  </ul>
  <div class="footer-rule"></div>
  <div class="copyright">Copyrights © 2018, Opal's RV Park &amp; Lodge. All rights reserved.</div>
  <div class="socials"><i></i><i></i><i></i><i></i></div>
</footer>

</body>
</html>
```